Design the 21st Golden Reel Indie Screen Week Poster. Think modern, chic, cool, film, movies - driving people to the film festival - the film festivla is in San Francisco and the SF East Bay. Our logo is attached. Dates will be determined soon . please use - November 2 - 11, 2018 (for placement) Keep in mind abstract, chic, modern - eye catching. website is www.grisw.example

Target Market(s)

25 - 45 year old - upper middle class

Industry/Entity Type

Film Production

Colors

Designer to choose colors to be used in the design.

Requirements
Must have
• logo (attached) www.grisw.example - chic modern design
Nice to have
• best coolest poster ever!
Should not have
• CLIP ART!!!

```html
<!DOCTYPE html>
<html lang="en">
<head>
<meta charset="utf-8">
<title>21st Golden Reel Indie Screen Week</title>
<link rel="stylesheet" href="https://fonts.googleapis.com/css2?family=Raleway:wght@400;700;800&family=Yellowtail&display=swap">
<style>
  :root {
    --paper: #e0e0e0;
    --numeral: #d3d3d3;
    --brand-red: #d43a3a;
    --ink: #1a1a1a;
    --mark-panel: #e5e5e5;
  }
  html, body {
    margin: 0;
    padding: 0;
    overflow: hidden;
  }
  .poster {
    position: relative;
    width: 776px;
    height: 1200px;
    background: var(--paper);
    overflow: hidden;
    font-family: "Raleway", sans-serif;
  }
  .anniversary-numeral {
    position: absolute;
    inset: 0;
  }
  .festival-title {
    position: absolute;
    left: 40px;
    top: 446px;
    margin: 0;
    color: var(--brand-red);
    font-weight: 800;
    font-size: 64px;
    line-height: 85px;
    letter-spacing: -0.5px;
  }
  .title-rule {
    position: absolute;
    left: 42px;
    top: 822px;
    width: 450px;
    height: 22px;
    background: var(--brand-red);
  }
  .festival-dates {
    position: absolute;
    left: 40px;
    top: 896px;
    margin: 0;
    color: var(--brand-red);
  }
  .festival-dates .days {
    display: block;
    font-weight: 400;
    font-size: 32px;
    line-height: 40px;
    letter-spacing: -0.5px;
  }
  .festival-dates .year {
    display: block;
    font-weight: 800;
    font-size: 58px;
    line-height: 70px;
  }
  .festival-site {
    position: absolute;
    left: 40px;
    top: 1030px;
    margin: 0;
    color: var(--brand-red);
    font-weight: 400;
    font-size: 22px;
  }
  .brand-panel {
    position: absolute;
    left: 486px;
    top: 966px;
    width: 276px;
    height: 234px;
    background: var(--mark-panel);
  }
  .brand-mark {
    position: absolute;
    left: 496px;
    top: 992px;
    width: 256px;
    text-align: center;
    color: var(--ink);
    font-weight: 700;
    font-size: 22px;
    line-height: 28px;
  }
  .brand-mark .dot {
    display: block;
    width: 44px;
    height: 44px;
    margin: 0 auto 14px;
    border-radius: 50%;
    background: var(--ink);
  }
</style>
</head>
<body>
  <main class="poster">
    <svg class="anniversary-numeral" width="776" height="1200" viewBox="0 0 776 1200" aria-hidden="true">
      <g transform="rotate(-16 380 430)">
        <text x="10" y="680" font-family="Raleway, sans-serif" font-weight="800" font-size="960" fill="var(--numeral)" textLength="680" lengthAdjust="spacingAndGlyphs">21</text>
      </g>
      <text x="560" y="180" font-family="Yellowtail, cursive" font-size="180" fill="var(--numeral)" transform="rotate(-16 610 120)">st</text>
    </svg>

    <h1 class="festival-title">Golden Reel<br>Indie<br>Screen<br>Week</h1>
    <div class="title-rule"></div>

    <p class="festival-dates">
      <span class="days">November 2 - 11</span>
      <span class="year">2018</span>
    </p>
    <p class="festival-site">www.grisw.example</p>

    <div class="brand-panel"></div>
    <div class="brand-mark">
      <span class="dot"></span>
      Golden Reel<br>Indie Screen Week
    </div>
  </main>
</body>
</html>
```